New Brazilian Craft Brewery Needs a Logo and Label Design.

We need a beer logo and label design for our new brazilian brewery. The brewery name is "MORVELHA" (that means holy in portuguese). The logo should have the words "MORVELHA" and "CERVEJAS ARTESANAIS" (craft beer). We would like a logo and label desings with something about holy theme like an angel drinking beer, a glass with wings, or anything else we are open to any new sugestion. We would like to see projects that are not the same tipical and classic beer desing. We like different, inovating, colorfull desings. Attached the are some old desings just for reference as we want something different.
Craft beer drinkers.
Brewery

```html
<!DOCTYPE html>
<html lang="pt">
<head>
<meta charset="utf-8">
<title>MORVELHA – India Pale Ale</title>
<link href="https://fonts.googleapis.com/css2?family=Arvo:wght@400;700&display=swap" rel="stylesheet">
<style>
  :root {
    --backdrop: #e9e5e3;
    --label-gold: #d6a93c;
    --deep-teal: #1f4b4b;
    --sky-teal: #9cc9c8;
    --cream: #fbf3dc;
    --ink-green: #2a5a3a;
  }
  * { box-sizing: border-box; margin: 0; padding: 0; }
  html, body {
    width: 1200px; height: 1000px; overflow: hidden;
    background: var(--backdrop);
    font-family: "Arvo", Georgia, serif;
  }
  .label {
    position: absolute; left: 390px; top: 50px; width: 420px;
    display: flex; flex-direction: column; align-items: center;
  }
  .brand {
    display: flex; flex-direction: column; align-items: center;
    width: 100%;
  }
  .brand-dot {
    width: 120px; height: 120px; border-radius: 50%;
    background: var(--sky-teal);
  }
  .brand-name {
    margin-top: 14px;
    font-weight: 700; font-size: 66px; letter-spacing: 1px;
    color: var(--deep-teal); line-height: 1;
  }
  .brand-band {
    margin-top: 14px; width: 480px; padding: 10px 0;
    background: var(--deep-teal); color: var(--cream);
    font-weight: 400; font-size: 26px; letter-spacing: 2px;
    text-align: center;
  }
  .panel {
    width: 420px; height: 640px;
    background: var(--label-gold);
    padding: 36px 34px 24px;
    display: flex; flex-direction: column;
  }
  .style-name {
    font-weight: 700; font-size: 96px; line-height: 1;
    color: var(--cream); letter-spacing: 3px;
  }
  .style-sub {
    font-weight: 400; font-size: 52px; line-height: 1.05;
    color: var(--cream); letter-spacing: 4px;
  }
  .beer-type {
    margin-top: 34px;
    font-weight: 700; font-size: 25px; color: var(--ink-green);
  }
  .beer-note {
    font-size: 13px; color: var(--ink-green);
  }
  .dotted-rule {
    margin: 14px 0;
    border-top: 8px dotted var(--ink-green);
  }
  .pairing-title {
    font-size: 20px; color: var(--cream);
  }
  .pairing-text {
    font-size: 17px; line-height: 1.35; color: var(--cream);
  }
  .facts {
    margin-top: auto;
    display: flex; justify-content: space-between;
    font-size: 14px; color: var(--ink-green);
  }
</style>
</head>
<body>
  <main class="label">
    <header class="brand">
      <div class="brand-dot"></div>
      <div class="brand-name">MORVELHA</div>
      <div class="brand-band">CERVEJAS ARTESANAIS</div>
    </header>
    <section class="panel">
      <h1 class="style-name">INDIA</h1>
      <h2 class="style-sub">PALE ALE</h2>
      <p class="beer-type">CERVECA CLARA FORTE</p>
      <p class="beer-note">puro malte com ingredientes selecionados</p>
      <div class="dotted-rule"></div>
      <p class="pairing-title">Fome?</p>
      <p class="pairing-text">combina bem com:<br>carnes vermelhas, queijos fortes<br>e pratos com sabores intensos.</p>
      <div class="dotted-rule"></div>
      <div class="facts"><span>600 ml</span><span>6,9% vol. alc.</span></div>
    </section>
  </main>
</body>
</html>
```